letter flyer TRADEUP

please see our website www.corvellpartners.com.au for details. however, we are a financial services company that has services in accounting and taxation, wealth advice, loan broking, general insurance and business advice. we want to target local potential business clients to focus on helping them conduct a review and work out what they need to do to improve the health and profitability of their business. we would like to create a letter/flyer to send them. we want the message to be as follows:
1) by having a review, we guarantee we will provide some financial benefit;
2) we are offering a cohesive and comprehensive team who will provide many financial services under one roof; and
3) we specialise in business.

we have called the campaign 'TRADEUP'

we have drafted a letter as a concept and we need design, any suggested changes in wording and imagery to demonstrate our message. We do have a logo for each of the divisions above. we thought the reverse side could just be our logo and catchphrase 'financial freedom is...'

***** we just want an A4 letter... not a bifold flyer
***** I have also included a copy of our newsletter so you can get the logos and feel for our business

```html
<!DOCTYPE html>
<html lang="en">
<head>
<meta charset="utf-8">
<title>Corvell Partners – TRADEUP flyer</title>
<link href="https://fonts.googleapis.com/css2?family=Lato:wght@400;700;900&family=Roboto+Condensed:wght@700&display=swap" rel="stylesheet">
<style>
  :root{
    --orange:#f58220;
    --orange-light:#f8a13a;
    --blue:#1a8fe0;
    --blue-deep:#0f6fc0;
    --navy:#0d2e4f;
    --ink:#3b3b3b;
    --dark:#1f2a36;
    --white:#ffffff;
    --gold:#d9a23c;
  }
  *{margin:0;padding:0;box-sizing:border-box}
  html,body{width:806px;height:1200px;overflow:hidden;background:var(--white)}
  .flyer{position:relative;width:806px;height:1200px;overflow:hidden;font-family:"Lato",sans-serif;color:var(--ink)}
  .shapes{position:absolute;inset:0}
  .abs{position:absolute}

  .brand{left:44px;top:40px;display:flex;align-items:center;gap:12px}
  .brand-dot{width:66px;height:66px;border-radius:50%;background:var(--blue-deep)}
  .brand-name{font-weight:700;font-size:22px;color:var(--navy);line-height:1.05;text-transform:uppercase}
  .brand-tagline{left:60px;top:116px;font-weight:900;font-size:12px;color:var(--gold);letter-spacing:.3px}
  .divider{left:257px;top:40px;width:2px;height:80px;background:#d5d9de}
  .call-out{left:287px;top:62px}
  .call-out .line1{font-weight:700;font-size:18px;color:var(--blue)}
  .call-out .line2{font-weight:700;font-size:24px;color:var(--dark);margin-top:2px}

  .hero-title{left:32px;top:222px;font-family:"Roboto Condensed",sans-serif;font-size:44px;color:var(--blue);text-transform:uppercase;line-height:1}
  .hero-sub{left:34px;top:272px;font-family:"Roboto Condensed",sans-serif;font-size:18px;text-transform:uppercase;line-height:1.4;letter-spacing:.2px}
  .hero-sub .white{color:var(--white)}
  .hero-sub .blue{color:var(--blue)}
  .questions{left:34px;top:376px;list-style:none;width:380px}
  .questions li{display:flex;align-items:flex-start;gap:14px;color:var(--white);font-weight:700;font-size:14.5px;line-height:1.3;margin-bottom:26px}
  .q-icon{flex:none;width:26px;height:26px;border-radius:50%;background:var(--blue);border:2px solid var(--white);display:flex;align-items:center;justify-content:center}
  .q-icon svg{width:13px;height:13px}

  .tag{height:30px;padding:0 26px 0 32px;background:var(--blue);color:var(--white);font-family:"Roboto Condensed",sans-serif;font-size:18px;display:flex;align-items:center;border-radius:0 16px 16px 0;text-transform:uppercase}
  .tag-about{left:0;top:620px}
  .tag-special{left:0;top:824px}
  .about-text{left:32px;top:666px;width:440px;font-size:13.6px;line-height:1.38;text-align:justify}
  .special-list{left:34px;top:872px;width:440px;list-style:none}
  .special-list li{position:relative;padding-left:18px;font-weight:700;font-size:14px;line-height:1.5;color:var(--dark);margin-bottom:4px}
  .special-list li::before{content:"";position:absolute;left:0;top:7px;width:7px;height:7px;border-radius:50%;background:var(--blue)}

  .offer-title{left:32px;top:1028px;font-family:"Roboto Condensed",sans-serif;font-size:24px;color:var(--blue);text-transform:uppercase;letter-spacing:.6px}
  .offer-sub{left:32px;top:1056px;font-family:"Roboto Condensed",sans-serif;font-size:15px;color:var(--dark);text-transform:uppercase}

  .meaning-title{left:532px;top:758px;color:var(--dark);font-family:"Roboto Condensed",sans-serif;font-size:30px;line-height:1.1}
  .meaning-title span{display:block;color:var(--white);font-size:27px}
  .meaning-rule{left:528px;top:830px;width:250px;height:2px;background:var(--white)}
  .meaning-list{left:532px;top:848px;width:250px;list-style:none}
  .meaning-list li{position:relative;padding-left:14px;color:var(--white);font-weight:700;font-size:13.6px;line-height:1.36;text-align:justify;margin-bottom:22px}
  .meaning-list li::before{content:"";position:absolute;left:0;top:6px;width:6px;height:6px;border-radius:50%;background:var(--white)}

  .contact{color:var(--white);font-weight:700;font-size:13.6px;display:flex;align-items:center;gap:8px}
  .contact svg{width:12px;height:12px}
  .contact-phone{left:34px;top:1134px}
  .contact-email{left:260px;top:1134px}
  .contact-web{left:34px;top:1162px}
</style>
</head>
<body>
<div class="flyer">
  <svg class="shapes" width="806" height="1200" viewBox="0 0 806 1200">
    <defs>
      <linearGradient id="heroGrad" x1="0" y1="0" x2="1" y2="0">
        <stop offset="0" stop-color="#f7931e"/>
        <stop offset="1" stop-color="#f9b04a"/>
      </linearGradient>
      <linearGradient id="panelGrad" x1="0" y1="0" x2="0" y2="1">
        <stop offset="0" stop-color="#1f99e8"/>
        <stop offset="1" stop-color="#0f7dd2"/>
      </linearGradient>
      <radialGradient id="photoGrad" cx="0.45" cy="0.5" r="0.6">
        <stop offset="0" stop-color="#f2f4f6"/>
        <stop offset="0.6" stop-color="#c8ced6"/>
        <stop offset="1" stop-color="#3a4452"/>
      </radialGradient>
    </defs>
    <!-- hero frame and panel -->
    <path d="M0,180 L470,180 L548,381 L470,582 L0,582" fill="none" stroke="var(--blue)" stroke-width="5"/>
    <path d="M0,192 L460,192 L534,381 L460,570 L0,570 Z" fill="url(#heroGrad)"/>
    <!-- right info panel -->
    <path d="M470,520 L806,520 L806,1200 L585,1200 L470,1000 Z" fill="url(#panelGrad)"/>
    <path d="M470,1000 L585,1200 L604,1200 L486,994 Z" fill="var(--orange)"/>
    <!-- circular frame -->
    <circle cx="640" cy="386" r="272" fill="var(--white)"/>
    <circle cx="640" cy="386" r="262" fill="none" stroke="var(--orange)" stroke-width="12"/>
    <circle cx="640" cy="386" r="246" fill="none" stroke="var(--blue)" stroke-width="8"/>
    <circle cx="640" cy="386" r="232" fill="url(#photoGrad)" role="img" aria-label="Photo of a businessman in a suit drawing a rising bar chart with an upward arrow"/>
    <!-- footer band -->
    <path d="M0,1112 L520,1112 L570,1200 L0,1200 Z" fill="var(--orange)"/>
    <g fill="#1b1b1b">
      <path d="M300,1200 L318,1182 L352,1182 L334,1200 Z"/>
      <path d="M350,1200 L368,1182 L402,1182 L384,1200 Z"/>
      <path d="M400,1200 L418,1182 L452,1182 L434,1200 Z"/>
    </g>
  </svg>

  <div class="abs brand"><span class="brand-dot"></span><span class="brand-name">Corvell<br>Partners</span></div>
  <div class="abs brand-tagline">YOUR WEALTH ADVISORS</div>
  <div class="abs divider"></div>
  <div class="abs call-out">
    <p class="line1">Simply call or email us</p>
    <p class="line2">And quote ‘tradeup’</p>
  </div>

  <h1 class="abs hero-title">Are you working</h1>
  <p class="abs hero-sub"><span class="white">Long hours and feel like you are not</span><br><span class="blue">reaping the benefits you should be?</span></p>
  <ul class="abs questions">
    <li><span class="q-icon"><svg viewBox="0 0 12 12"><rect x="1" y="4" width="10" height="7" fill="#fff"/><rect x="4" y="2" width="4" height="2" fill="none" stroke="#fff"/></svg></span>Do you have work life balance?</li>
    <li><span class="q-icon"><svg viewBox="0 0 12 12"><circle cx="6" cy="3" r="1.5" fill="#fff"/><rect x="5" y="5" width="2" height="6" fill="#fff"/></svg></span>Do you understand your business-<br>es strengths and weaknesses?</li>
    <li><span class="q-icon"><svg viewBox="0 0 12 12"><rect x="1" y="7" width="2" height="4" fill="#fff"/><rect x="5" y="4" width="2" height="7" fill="#fff"/><rect x="9" y="1" width="2" height="10" fill="#fff"/></svg></span>Do you feel like you have potential<br>to grow?</li>
  </ul>

  <h2 class="abs tag tag-about">About us</h2>
  <p class="abs about-text">Our business is to help you better understand your business and help you to prepare unique strategies to improve the success and value of your business. We can assist to streamline your financial service relationships, providing all financial services under one roof. Such as, accounting and taxation, business planning, wealth planning, smsf, insurance, loan broking, general insurance and business planning.</p>

  <h2 class="abs tag tag-special">Specialised in</h2>
  <ul class="abs special-list">
    <li>By having a review, we guarantee<br>we will provide some financial benefit</li>
    <li>We are offering a cohesive and comprehensive team<br>who will provide many financial services under one roof</li>
    <li>We specialise in business</li>
  </ul>

  <h2 class="abs offer-title">How to take advantage</h2>
  <p class="abs offer-sub">of your initial complimentary business check</p>

  <h2 class="abs meaning-title">What does this <span>mean for you?</span></h2>
  <div class="abs meaning-rule"></div>
  <ul class="abs meaning-list">
    <li>Coordinated approach and one simple phone call to meet your financial requiremnts. This saves you time and effort</li>
    <li>A financial services team working together for your business review will ensure you have savings and maximise your financial position with a solid team behind you, all coordinated and on the same team</li>
  </ul>

  <p class="abs contact contact-phone"><svg viewBox="0 0 12 12"><path d="M2,1 L4.5,1 L5.5,3.5 L4,4.5 Q5,7 7.5,8 L8.5,6.5 L11,7.5 L11,10 Q6,11 2,6 Q1,3 2,1 Z" fill="#fff"/></svg>1300 555 018</p>
  <p class="abs contact contact-email"><svg viewBox="0 0 12 12"><rect x="1" y="2.5" width="10" height="7" fill="#fff"/><path d="M1,2.5 L6,6.5 L11,2.5" fill="none" stroke="#f58220"/></svg>info@corvellpartners.com.au</p>
  <p class="abs contact contact-web"><svg viewBox="0 0 12 12"><rect x="1" y="2" width="10" height="8" rx="1" fill="#fff"/></svg>www.corvellpartners.com.au</p>
</div>
</body>
</html>
```